Harrowgate Supply Group Business Card Design

The Business Card will be one side only with Harrowgate Supplies Group Logo
Card should have:
Name
Title
Office phone Number
Cell Number
email address
Website
Street Address
Our Slogan is Rugged and Reliable
Looking for something that stands out from other business cards

Target Market(s)

Heavy equipment Lease Company

```html
<!DOCTYPE html>
<html lang="en">
<head>
<meta charset="utf-8">
<title>Harrowgate Supplies Group – Business Card</title>
<link rel="stylesheet" href="https://fonts.googleapis.com/css2?family=Montserrat:wght@600;700&family=Work+Sans:wght@400;500&display=swap">
<style>
  :root {
    --navy: #27297a;
    --red: #d7202f;
    --white: #ffffff;
    --ink: #3d3d45;
    --stage: #a9a9a9;
  }
  * { box-sizing: border-box; margin: 0; padding: 0; }
  html, body { width: 1200px; height: 930px; overflow: hidden; }
  body {
    background: var(--stage);
    font-family: "Work Sans", Arial, sans-serif;
    position: relative;
  }
  .card {
    position: absolute;
    width: 540px;
    height: 310px;
    border-radius: 22px;
    overflow: hidden;
    box-shadow: 0 6px 16px rgba(0,0,0,.25);
  }
  /* Front */
  .card-front {
    left: 80px; top: 150px;
    background: var(--navy);
    color: var(--white);
  }
  .front-brand {
    position: absolute;
    left: 0; right: 0; top: 118px;
    display: flex; align-items: center; justify-content: center; gap: 14px;
  }
  .brand-square {
    width: 26px; height: 26px;
    background: var(--white);
  }
  .front-brand .brand-name {
    font-family: "Montserrat", Arial, sans-serif;
    font-weight: 700;
    font-size: 30px;
    letter-spacing: .5px;
    color: var(--white);
  }
  .slogan {
    position: absolute;
    left: 0; right: 0; bottom: 40px;
    text-align: center;
    font-family: "Montserrat", Arial, sans-serif;
    font-weight: 600;
    font-size: 15px;
    letter-spacing: 3.5px;
  }
  /* Back */
  .card-back {
    left: 580px; top: 470px;
    background: var(--white);
    color: var(--ink);
  }
  .back-brand {
    position: absolute;
    left: 32px; top: 52px;
    display: flex; align-items: center; gap: 10px;
  }
  .brand-dot {
    flex: none;
    width: 18px; height: 18px; border-radius: 50%;
    background: var(--navy);
  }
  .back-brand .brand-name {
    width: 210px;
    font-family: "Montserrat", Arial, sans-serif;
    font-weight: 700;
    font-size: 16px;
    line-height: 1.15;
    color: var(--red);
  }
  .person {
    position: absolute;
    right: 34px; top: 40px;
    text-align: right;
  }
  .person-name {
    font-family: "Montserrat", Arial, sans-serif;
    font-weight: 700;
    font-size: 22px;
    color: var(--navy);
    white-space: nowrap;
  }
  .person-title { font-size: 13px; margin-top: 2px; }
  .divider {
    position: absolute;
    left: 32px; right: 34px; top: 118px;
    border-top: 1.5px solid var(--navy);
  }
  .contacts {
    position: absolute;
    left: 32px; top: 138px;
    list-style: none;
    font-size: 14px;
    line-height: 21px;
  }
  .contacts li { display: flex; align-items: center; gap: 8px; }
  .contacts svg { width: 11px; height: 11px; fill: var(--navy); }
  .contacts .web { color: var(--navy); font-weight: 500; }
  .address {
    position: absolute;
    right: 34px; top: 138px;
    text-align: right;
    font-size: 13.5px;
    line-height: 20px;
  }
  .wave { position: absolute; left: 0; bottom: 0; width: 540px; height: 140px; }
</style>
</head>
<body>

<section class="card card-front">
  <div class="front-brand">
    <span class="brand-square"></span>
    <span class="brand-name">HARROWGATE PUMPS</span>
  </div>
  <p class="slogan">RUGGED AND RELIABLE</p>
</section>

<section class="card card-back">
  <div class="back-brand">
    <span class="brand-dot"></span>
    <span class="brand-name">HARROWGATE SUPPLIES GROUP</span>
  </div>

  <div class="person">
    <p class="person-name">DANIEL REEVES</p>
    <p class="person-title">Director</p>
  </div>

  <div class="divider"></div>

  <ul class="contacts">
    <li><svg viewBox="0 0 12 12"><path d="M2.5 1l2 2-1 1.3c.7 1.5 1.8 2.6 3.2 3.2L8 6.5l2 2-1.5 1.8C5 10 2 7 1.2 2.5z"/></svg>(555) 014-2871</li>
    <li><svg viewBox="0 0 12 12"><path d="M3.5 0h5a1 1 0 0 1 1 1v10a1 1 0 0 1-1 1h-5a1 1 0 0 1-1-1V1a1 1 0 0 1 1-1zm.5 2v7h4V2z"/></svg>(555) 019-6630</li>
    <li><svg viewBox="0 0 12 12"><path d="M0 2h12v8H0zm1.2 1.2v.3L6 6.6l4.8-3.1v-.3zm0 1.7v4h9.6v-4L6 8z"/></svg>info@harrowgategroup.com</li>
    <li class="web"><svg viewBox="0 0 12 12"><circle cx="6" cy="6" r="5.5"/></svg>www.harrowgategroup.com</li>
  </ul>

  <p class="address">212b Kestrel Road,<br>Ashford, NZ, 8042</p>

  <svg class="wave" viewBox="0 0 540 140" preserveAspectRatio="none" aria-hidden="true">
    <path d="M0 140 L0 128 C150 120 260 90 360 50 C430 22 490 10 540 8 L540 140 Z" fill="var(--navy)"/>
    <path d="M0 124 C150 116 260 84 358 44 C428 16 490 4 540 2 L540 7 C490 9 430 20 362 48 C262 88 150 120 0 129 Z" fill="var(--red)"/>
  </svg>
</section>

</body>
</html>
```